REAL PSYCHIC rear window decal. Mystical, light, positive, spiritual coach vibes

Design a sign for my back car window.
HOT PINK and purple swirly, mystical sign. Eye-catching and classy.
Size 24” x 18”
TEXT:
MARISOL DEANE
Psychic & Medium
Www,.marisoldeane.com
World Renowned for Over 45 Years. (This last line make small at bottom)

*This is not a filled in magnet, it will be transparent.

Target Market(s)

Women

Industry/Entity Type

Spirituality

Font styles to use
Script
Other font styles liked:
• See upload for a font I like

Colors
E54698
E96AAD
F1A4CE
F9D9EA
FCEFF6
A7469A
B969AE
D3A5CF
EDDBEB
F8F0F9
6B429C
8869AF
B7A5CE
E3DAEB
F3F0F8

Requirements
Must have
• Pink purple, classy yet mystical vibe
Nice to have
• Easy to read, but old-timey classic font for “MARISOL DEANE”

```html
<!DOCTYPE html>
<html lang="en">
<head>
<meta charset="utf-8">
<title>Marisol Deane – Psychic &amp; Medium Window Decal</title>
<link href="https://fonts.googleapis.com/css2?family=Almendra:wght@400;700&display=swap" rel="stylesheet">
<style>
  :root {
    --decal-white: #ffffff;
    --plum: #8f2a8d;
    --hot-pink: #e5127f;
    --blush: #fbe3e7;
    --blush-deep: #f8d6dc;
  }
  html, body {
    margin: 0;
    padding: 0;
    width: 1200px;
    height: 829px;
    overflow: hidden;
    background: var(--decal-white);
  }
  .decal {
    position: relative;
    width: 1200px;
    height: 829px;
    background: var(--decal-white);
    overflow: hidden;
  }
  .decal__art {
    position: absolute;
    inset: 0;
    width: 1200px;
    height: 829px;
  }
  .wash { fill: var(--blush); }
  .wash--deep { fill: var(--blush-deep); }
  .flourish { fill: var(--hot-pink); opacity: 0.85; }
  .name {
    font-family: "Almendra", Georgia, serif;
    font-weight: 700;
    fill: var(--plum);
  }
  .tagline, .web {
    font-family: "Almendra", Georgia, serif;
    font-weight: 700;
    fill: var(--hot-pink);
  }
  .renown {
    font-family: "Almendra", Georgia, serif;
    font-weight: 700;
    fill: var(--plum);
  }
</style>
</head>
<body>
<main class="decal">
  <svg class="decal__art" viewBox="0 0 1200 829" xmlns="http://www.w3.org/2000/svg">
    <!-- soft background washes -->
    <path class="wash" d="M740 0 H1200 V829 H430 C420 760 440 680 560 640 C700 600 800 640 900 610 C960 580 930 500 920 420 C910 320 930 250 900 180 C870 110 790 80 760 40 Z"/>
    <path class="wash--deep" d="M0 470 C80 450 180 430 260 430 L240 450 C300 445 330 455 350 470 C260 500 170 540 0 570 Z"/>
    <path class="wash--deep" d="M900 520 C980 500 1080 505 1200 520 V620 C1110 600 1010 590 930 560 C960 550 990 545 1010 540 C960 535 925 530 900 520 Z"/>

    <!-- ornamental flourish dividers -->
    <rect class="flourish" x="103" y="170" width="996" height="34" rx="17" role="img" aria-label="Ornamental pink swirl flourish divider with heart at centre"/>
    <rect class="flourish" x="103" y="612" width="996" height="34" rx="17" role="img" aria-label="Ornamental pink swirl flourish divider with heart at centre"/>

    <!-- lettering -->
    <text class="name" x="603" y="409" text-anchor="middle" font-size="160" textLength="906" lengthAdjust="spacingAndGlyphs">Marisol Deane</text>
    <text class="tagline" x="603" y="494" text-anchor="middle" font-size="54" textLength="446" lengthAdjust="spacingAndGlyphs">Psychic &amp; Medium</text>
    <text class="web" x="603" y="552" text-anchor="middle" font-size="54" textLength="518" lengthAdjust="spacingAndGlyphs">www.marisoldeane.com</text>
    <text class="renown" x="603" y="772" text-anchor="middle" font-size="28" textLength="444" lengthAdjust="spacingAndGlyphs">World Renowned for Over 45 Years.</text>
  </svg>
</main>
</body>
</html>
```